Zielgruppe
Wir unterstützen dich in deiner persönlichen Entwicklung ihrer Stresskompetenzen durch Training, Coaching, Weiterbildungen und komplementären Behandlungsmethoden.
Stresskompetenzen sind erlernbare Fähigkeiten, persönliche Eigenschaften und trainierbare innere Zustände, welche deine psychische Widerstandskraft, Belastbarkeit und Flexibilität im Umgang mit schwierigen Situationen und Lebensereignissen steigern.
Wir unterscheiden uns von anderen Coaches, weil wir nicht irgendeine Methode in den Vordergrund stellen. Wir verstehen uns als fundierte Praktiker und wählen aus verschiedenen Therapie-, Coaching- und Trainingskonzepten jene Werkzeuge aus, mit denen unsere Kunden in ihrer Stressthematik die besten Erfolge erzielen.
Aufgabenstellung
Es gibt ein bestehendes Logo 'kernfokus-praxis.ch'. Die neue Unternehmung geht aus dieser hervor. Die Grundidee mit dem Löwenkopf der aus zwei Hirnhälften besteht soll wenn möglich bestehen bleiben.

```html
<!DOCTYPE html>
<html lang="de">
<head>
<meta charset="utf-8">
<title>Gelassenwerk – Geschäftsausstattung</title>
<link href="https://fonts.googleapis.com/css2?family=Cinzel:wght@600&family=Montserrat:wght@400;500&display=swap" rel="stylesheet">
<style>
  :root{
    --stage:#020a14;
    --ink:#0d0d0f;
    --teal:#05809d;
    --teal-dark:#0a4e5f;
    --paper:#ffffff;
    --mat:#dcdcdc;
    --grey-text:#444;
    --logo-light:#f2f2f2;
  }
  *{box-sizing:border-box;margin:0;padding:0}
  html,body{width:1200px;height:927px;overflow:hidden;background:var(--stage)}
  .sheet{position:relative;width:1200px;height:927px}
  .brand-panel{position:absolute;top:0;height:335px;width:339px;display:flex;flex-direction:column;align-items:center;justify-content:center}
  .brand-panel--dark{left:262px;background:var(--ink)}
  .brand-panel--teal{left:601px;width:338px;background:var(--teal)}
  .mat{position:absolute;left:262px;top:335px;width:677px;height:592px;background:var(--mat)}
  .wordmark{font-family:"Cinzel",serif;font-weight:600;color:var(--logo-light);letter-spacing:.5px;white-space:nowrap;line-height:1.2}
  .tagline{font-family:"Cinzel",serif;font-weight:600;color:var(--logo-light);white-space:nowrap;line-height:1.2}
  .mark-dot{border-radius:50%;background:var(--logo-light);flex:none}
  .brand-panel--dark .mark-dot{background:var(--teal)}
  .brand-panel .mark-dot{width:78px;height:78px;margin-bottom:22px;margin-top:-14px}
  .brand-panel .wordmark{font-size:21px}
  .brand-panel .tagline{font-size:11px;margin-top:8px}

  .card{position:absolute;width:295px;height:169px}
  .card--front{left:285px;top:358px;background:var(--paper)}
  .card--back{left:621px;top:358px;background:var(--teal);display:flex;flex-direction:column;align-items:center;justify-content:center}
  .card--back .mark-dot{width:40px;height:40px;margin-bottom:12px}
  .card--back .wordmark{font-size:12.5px}
  .card--back .tagline{font-size:6.5px;margin-top:4px}
  .card-logo{position:absolute;left:0;right:0;top:16px;display:flex;flex-direction:column;align-items:center}
  .card-logo .mark-dot{width:26px;height:26px;background:var(--teal);margin-bottom:5px}
  .card-logo .wordmark{font-size:8.5px;color:var(--teal)}
  .card-logo .tagline{font-size:4.5px;color:var(--teal);margin-top:2px}
  .holder{position:absolute;left:20px;top:88px;font-family:"Montserrat",sans-serif}
  .holder-name{font-size:11.5px;color:var(--teal);letter-spacing:.5px;text-transform:uppercase}
  .holder-role{font-size:6px;color:var(--grey-text)}
  .card-rule{position:absolute;left:20px;width:252px;top:113px;height:1px;background:var(--teal)}
  .contact{position:absolute;left:22px;top:120px;list-style:none;font-family:"Montserrat",sans-serif;font-size:8px;color:#222}
  .contact li{display:flex;align-items:center;gap:6px;height:12px}
  .contact svg{width:8px;height:8px}
  .card-band{position:absolute;left:0;right:0;bottom:0;height:10px;background:var(--teal);border-bottom:4px solid var(--teal-dark)}

  .envelope{position:absolute;left:295px;width:317px;height:161px;background:var(--paper);box-shadow:2px 3px 6px rgba(0,0,0,.25);overflow:hidden}
  .envelope--front{top:566px}
  .envelope--back{top:744px}
  .small-logo{display:flex;align-items:center;gap:4px}
  .small-logo .mark-dot{width:17px;height:17px;background:var(--teal)}
  .small-logo .wordmark{font-size:7.5px;color:var(--teal)}
  .small-logo .tagline{font-size:4px;color:var(--teal)}
  .envelope--front .small-logo{position:absolute;left:21px;top:15px}
  .env-rule{position:absolute;left:21px;right:10px;top:48px;height:1px;background:var(--teal)}
  .address{font-family:"Montserrat",sans-serif;font-size:6px;line-height:6.2px;color:var(--grey-text)}
  .envelope--front .address{position:absolute;left:21px;top:59px}
  .window{position:absolute;left:22px;top:97px;width:81px;height:37px;background:#e5e5e5;border-radius:3px}
  .flap{position:absolute;left:0;top:0;width:317px;height:48px}
  .envelope--back .small-logo{position:absolute;left:115px;top:12px}
  .envelope--back .mark-dot{background:var(--paper)}
  .envelope--back .wordmark,.envelope--back .tagline{color:var(--paper)}

  .letterhead{position:absolute;left:637px;top:566px;width:263px;height:344px;background:var(--paper);box-shadow:5px 5px 0 #9a9a9a}
  .letterhead .small-logo{position:absolute;left:22px;top:16px}
  .letterhead .address{position:absolute;right:12px;top:10px;text-align:right}
  .lh-rule{position:absolute;left:0;right:0;top:50px;height:1px;background:var(--teal)}
  .lh-foot{position:absolute;left:0;right:0;bottom:32px;height:1px;background:#8a8a8a}
</style>
</head>
<body>
<main class="sheet">
  <section class="brand-panel brand-panel--dark">
    <div class="mark-dot"></div>
    <p class="wordmark">GELASSENWERK.CH</p>
    <p class="tagline">RUHIG IM KOPF - STARK IM HANDELN</p>
  </section>
  <section class="brand-panel brand-panel--teal">
    <div class="mark-dot"></div>
    <p class="wordmark">GELASSENWERK.CH</p>
    <p class="tagline">RUHIG IM KOPF - STARK IM HANDELN</p>
  </section>

  <div class="mat"></div>

  <article class="card card--front">
    <div class="card-logo">
      <div class="mark-dot"></div>
      <p class="wordmark">GELASSENWERK.CH</p>
      <p class="tagline">RUHIG IM KOPF - STARK IM HANDELN</p>
    </div>
    <div class="holder">
      <p class="holder-name">Nora Keller</p>
      <p class="holder-role">Managing Director</p>
    </div>
    <div class="card-rule"></div>
    <ul class="contact">
      <li><svg viewBox="0 0 8 8"><circle cx="4" cy="4" r="4" fill="#0a4e5f"/><path d="M2.6 2c.4 1.8 1.6 3.2 3.4 3.8l-.6.6C3.6 5.8 2.2 4.4 1.8 2.6z" fill="#fff"/></svg>0117 440 2719</li>
      <li><svg viewBox="0 0 8 8"><circle cx="4" cy="4" r="4" fill="#0a4e5f"/><rect x="2" y="2.7" width="4" height="2.8" fill="none" stroke="#fff" stroke-width=".6"/></svg>nora@gelassenwerk.ch</li>
      <li><svg viewBox="0 0 8 8"><circle cx="4" cy="4" r="4" fill="#0a4e5f"/><circle cx="4" cy="4" r="2" fill="none" stroke="#fff" stroke-width=".6"/></svg>gelassenwerk.ch</li>
    </ul>
    <div class="card-band"></div>
  </article>

  <article class="card card--back">
    <div class="mark-dot"></div>
    <p class="wordmark">GELASSENWERK.CH</p>
    <p class="tagline">RUHIG IM KOPF - STARK IM HANDELN</p>
  </article>

  <article class="envelope envelope--front">
    <div class="small-logo">
      <div class="mark-dot"></div>
      <div><p class="wordmark">GELASSENWERK.CH</p><p class="tagline">RUHIG IM KOPF - STARK IM HANDELN</p></div>
    </div>
    <div class="env-rule"></div>
    <p class="address">Gelassenwerk<br>Seefeld Business Park<br>Seefeldstrasse 12<br>Zürich<br>CH 8008</p>
    <div class="window"></div>
  </article>

  <article class="envelope envelope--back">
    <svg class="flap" viewBox="0 0 317 48" preserveAspectRatio="none"><path d="M0 0H317V6Q312 38 290 38H27Q5 38 0 6Z" fill="var(--teal)"/></svg>
    <div class="small-logo">
      <div class="mark-dot"></div>
      <div><p class="wordmark">GELASSENWERK.CH</p><p class="tagline">RUHIG IM KOPF - STARK IM HANDELN</p></div>
    </div>
  </article>

  <article class="letterhead">
    <div class="small-logo">
      <div class="mark-dot"></div>
      <div><p class="wordmark">GELASSENWERK.CH</p><p class="tagline">RUHIG IM KOPF - STARK IM HANDELN</p></div>
    </div>
    <p class="address">Gelassenwerk<br>Seefeld Business Park<br>Seefeldstrasse 12<br>Zürich<br>CH 8008</p>
    <div class="lh-rule"></div>
    <div class="lh-foot"></div>
  </article>
</main>
</body>
</html>
```